Thorne Consulting, Business Cards for International Development Consultancy

I'm an independent consultant working in the international development sector. I work with small organisations in developing countries to help them develop their community based programs so that they can be internationally competitive. This means they need to work better with their own communities to deliver meaningful quality work and also improve the accountability of their work so that they can compete for international and domestic funding.

I like the idea of being a connector between community, local organisations and international best practice and back again (ie acknowledging that international best practice can learn a lot from community).

My surname is Thorne - so I'd like the logo to use the idea of web as a connector.

I work with people with sight impairments - would like my card to be useful for low vision (i.e. clear graphics, easy to read font) and no vision (i.e. brail).

Target Market(s)

international non-government organisations (i.e. harvestaid, bright futures trust, open horizons), Blue Anchor Relief Alliance, government (i.e. Australian Bureau of Overseas Partnerships, consulars), non government agencies,

Industry/Entity Type

Business

Contact Information for Business Card

International Development Consultant
Connecting International Development with Community

Kerry Thorne
Lead Consultant
Phone: +61 417 382519
Email: kthorne.consulting@mailvale.com

Font styles to use
Sans Serif

Colors
eaf1f7
85acd3
d3a5cc
0456a4
a64599
0255a3

Requirements
Nice to have
• brail
Should not have
• fancy fonts - needs to be easy to read.

```html
<!DOCTYPE html>
<html lang="en">
<head>
<meta charset="utf-8">
<title>Thorne Consulting – Business Cards</title>
<link rel="stylesheet" href="https://fonts.googleapis.com/css2?family=Montserrat:wght@400;500;600;700&display=swap">
<style>
  :root {
    --backdrop: #eceef2;
    --brand-blue: #2d35ad;
    --brand-blue-deep: #252c94;
    --pattern-tone: #3a3fb4;
    --ink: #3b3a8f;
    --ink-soft: #8a8f9a;
    --card-white: #fbfbfc;
    --stripe-tone: #eeeef1;
    --on-blue: #ffffff;
  }
  * { box-sizing: border-box; margin: 0; padding: 0; }
  html, body {
    width: 1200px; height: 800px; overflow: hidden;
    background: var(--backdrop);
    font-family: "Montserrat", Arial, sans-serif;
  }
  .canvas { position: relative; width: 1200px; height: 800px; }
  .card {
    position: absolute; top: 242px;
    width: 520px; height: 316px;
    border-radius: 4px; overflow: hidden;
    box-shadow: 0 6px 18px rgba(30, 35, 60, 0.18);
  }

  /* Back of card */
  .card-back { left: 60px; background: var(--brand-blue); }
  .card-back .pattern-field {
    position: absolute; inset: 0;
    background: radial-gradient(circle at 50% 45%, var(--pattern-tone), var(--brand-blue-deep));
  }
  .brand-block {
    position: absolute; inset: 0;
    display: flex; flex-direction: column; align-items: center; justify-content: center;
    color: var(--on-blue); text-align: center;
  }
  .brand-mark {
    width: 70px; height: 70px; border-radius: 50%;
    border: 3px solid var(--on-blue); margin-bottom: 18px;
  }
  .brand-name { font-weight: 700; font-size: 64px; line-height: 0.95; letter-spacing: 1px; }
  .brand-sub { font-weight: 700; font-size: 40px; line-height: 1.05; }
  .brand-role {
    margin-top: 12px; font-weight: 500; font-size: 11.5px; letter-spacing: 1.4px;
  }

  /* Front of card */
  .card-front { left: 620px; background: var(--card-white); }
  .stripe-field {
    position: absolute; inset: 0;
    background: linear-gradient(120deg, var(--card-white) 35%, var(--stripe-tone) 100%);
  }
  .person { position: absolute; left: 30px; top: 28px; }
  .person-name {
    font-weight: 700; font-size: 25px; letter-spacing: 4px; color: var(--ink);
  }
  .person-title {
    font-weight: 500; font-size: 12.5px; letter-spacing: 2px; color: var(--ink-soft); margin-top: 2px;
  }
  .contacts {
    position: absolute; right: 26px; top: 172px;
    list-style: none; text-align: right;
  }
  .contacts li {
    display: flex; align-items: center; justify-content: flex-end; gap: 10px;
    font-size: 16px; font-weight: 500; color: var(--ink); height: 26px;
  }
  .contact-icon {
    width: 20px; height: 20px; border-radius: 50%; background: var(--ink);
    display: flex; align-items: center; justify-content: center;
  }
  .tagline {
    position: absolute; left: 30px; bottom: 24px;
    font-size: 11.5px; font-weight: 500; letter-spacing: 0.9px; color: var(--ink);
    white-space: nowrap;
  }
</style>
</head>
<body>
<main class="canvas">

  <section class="card card-back" aria-label="Card back">
    <div class="pattern-field" role="img" aria-label="Tonal field of interlocking concentric polygon rings in deep blue"></div>
    <div class="brand-block">
      <div class="brand-mark" aria-hidden="true"></div>
      <div class="brand-name">Thorne</div>
      <div class="brand-sub">Consulting</div>
      <div class="brand-role">INTERNATIONAL DEVELOPMENT CONSULTANT</div>
    </div>
  </section>

  <section class="card card-front" aria-label="Card front">
    <div class="stripe-field" role="img" aria-label="Faint light grey chevron stripe pattern across the card"></div>

    <div class="person">
      <div class="person-name">KERRY THORNE</div>
      <div class="person-title">LEAD CONSULTANT</div>
    </div>

    <ul class="contacts">
      <li>+61 417 382519
        <span class="contact-icon">
          <svg width="10" height="13" viewBox="0 0 10 13" aria-hidden="true"><rect x="1" y="0.8" width="8" height="11.4" rx="1.5" fill="none" stroke="#fff" stroke-width="1.4"/><circle cx="5" cy="10" r="0.9" fill="#fff"/></svg>
        </span>
      </li>
      <li>kthorne.consulting
        <span class="contact-icon">
          <svg width="12" height="11" viewBox="0 0 12 11" aria-hidden="true"><path d="M1.5 1h9a0.8 0.8 0 0 1 0.8 0.8v5.2a0.8 0.8 0 0 1-0.8 0.8H5l-2.6 2.2V7.8H1.5a0.8 0.8 0 0 1-0.8-0.8V1.8A0.8 0.8 0 0 1 1.5 1z" fill="none" stroke="#fff" stroke-width="1.2" stroke-linejoin="round"/></svg>
        </span>
      </li>
      <li>kthorne.consulting@mailvale.com
        <span class="contact-icon">
          <svg width="12" height="9" viewBox="0 0 12 9" aria-hidden="true"><rect x="0.7" y="0.7" width="10.6" height="7.6" fill="none" stroke="#fff" stroke-width="1.3"/><polyline points="0.7,0.7 6,5 11.3,0.7" fill="none" stroke="#fff" stroke-width="1.3"/></svg>
        </span>
      </li>
    </ul>

    <p class="tagline">CONNECTING INTERNATIONAL DEVELOPMENT WITH COMMUNITY</p>
  </section>

</main>
</body>
</html>
```